Vessa Kliniq - Dermatology Consultation App

Vessa Kliniq is launching a new Pindle IOS App for online Dermatology consultation. We would appreciate a simple Scandinavian design which communicates trust, comfort and expensive feel. Most yacht designs have similar color palette, light wood colors and textures, but don’t be restricted by those in your artistic search.
The process is completed in three easy steps:
1. take a Snapshot.
2. Describe and Send it.
3. get Diagnosis and Treatment.
The Home screen should also have buttons - Start new Case, Follow up Visit, Rx Refill.
15% of the Home screen should also have a field/button - Medical Cosmetics Shop.
10% of the Home screen should also have a field or buttons for Our Partners (sponsors) – Lumavel, Norvexa, Toral, Ostra. (if you click you would be directed to their sites)
Note / Suggestion : Maybe you could use a larger picture of a dermatologist and have overlying fields and content, just for more influencing effect. (I am not a professional though)
Thank you so much.
24 - 59 Female
Club

```html
<!DOCTYPE html>
<html lang="en">
<head>
<meta charset="utf-8">
<title>Vessa Kliniq – Dermatology Consultation App</title>
<link href="https://fonts.googleapis.com/css2?family=Montserrat:wght@300;400;500;600;700&display=swap" rel="stylesheet">
<style>
  :root {
    --stage: #b9c1c9;
    --plum: #4b2b3b;
    --plum-text: #3d2733;
    --ink: #2a2228;
    --muted: #6d6469;
    --screen: #ffffff;
    --panel: #f3f2f3;
    --shop: #ddd8db;
    --rule: #e3dfe1;
    --dot: #d9d4d6;
  }
  * { box-sizing: border-box; margin: 0; padding: 0; }
  html, body { width: 1200px; height: 1100px; overflow: hidden; }
  body {
    background: var(--stage);
    font-family: "Montserrat", sans-serif;
    color: var(--ink);
    position: relative;
  }
  .app-screens {
    position: absolute; top: 160px; left: 30px;
    display: flex; gap: 30px;
  }
  .screen {
    width: 360px; height: 780px; background: var(--screen);
    display: flex; flex-direction: column; overflow: hidden;
  }
  .screen > * { flex-shrink: 0; }
  .status-bar {
    height: 40px; display: flex; align-items: center; justify-content: space-between;
    padding: 0 14px; font-size: 15px; font-weight: 500; color: var(--ink);
  }
  .status-left { display: flex; align-items: center; gap: 4px; }
  .status-right { display: flex; align-items: center; gap: 6px; min-width: 80px; justify-content: flex-end; }
  .signal { letter-spacing: -1px; font-size: 11px; }
  .nav-bar {
    height: 56px; display: flex; align-items: center; padding: 0 14px;
    border-bottom: 3px solid var(--rule); position: relative;
    font-size: 17px; font-weight: 500; letter-spacing: .5px;
  }
  .nav-back { display: flex; align-items: center; gap: 8px; color: var(--ink); font-weight: 400; }
  .nav-title { position: absolute; left: 50%; transform: translateX(-42%); white-space: nowrap; }
  .nav-search { margin-left: auto; }

  .hero { position: relative; height: 300px; }
  .hero-photo { position: absolute; inset: 0; }
  .hero-photo.face { background: linear-gradient(100deg, #eef0f1 0%, #e6e4e3 45%, #d8c6bd 72%, #c9ab9c 100%); }
  .hero-photo.exam { background: linear-gradient(100deg, #e3e7ea 0%, #d9c6b8 40%, #c99a80 62%, #3a3234 82%, #e9ecef 100%); }
  .hero-content { position: absolute; left: 18px; top: 60px; width: 170px; text-align: center; }
  .brand { display: flex; align-items: center; justify-content: center; gap: 8px; }
  .brand-mark { width: 30px; height: 30px; border-radius: 50%; border: 2px solid var(--plum-text); flex-shrink: 0; }
  .brand-name { font-size: 19px; font-weight: 500; color: var(--plum-text); white-space: nowrap; }
  .brand-tag { font-size: 10px; font-weight: 500; margin-top: 8px; color: var(--plum-text); letter-spacing: .3px; }
  .hero-heading { margin-top: 50px; font-size: 26px; font-weight: 700; line-height: 1.3; color: var(--plum-text); letter-spacing: .5px; }
  .carousel-dots { position: absolute; bottom: 20px; left: 0; right: 0; display: flex; justify-content: center; gap: 14px; }
  .carousel-dots span { width: 11px; height: 11px; border-radius: 50%; background: var(--dot); }
  .carousel-dots span.active { background: var(--plum); }
  .exam .carousel-dots span.active { background: #fff; }

  .menu { list-style: none; }
  .menu li {
    height: 70px; display: flex; align-items: center; justify-content: space-between;
    padding: 0 22px; font-size: 25px; font-weight: 300; color: var(--plum-text);
    border-bottom: 2px solid var(--rule); white-space: nowrap;
  }
  .shop-band {
    height: 104px; background: var(--shop); display: flex; align-items: center; justify-content: center;
    padding: 0 14px; white-space: nowrap;
    font-size: 25px; font-weight: 300; color: var(--plum-text); letter-spacing: .2px;
  }
  .shop-band.long { font-size: 23px; letter-spacing: 0; }
  .partners {
    height: 70px; background: var(--plum); display: flex; align-items: center; justify-content: space-evenly;
    color: #fff; font-size: 19px; font-weight: 500; letter-spacing: 1px;
  }
  .partners a { color: inherit; text-decoration: none; }
  .screen-foot { flex: 1 1 auto; background: var(--panel); }

  .mail { flex: 1 1 auto; min-height: 0; overflow: hidden; background: var(--panel); padding: 20px 22px 0; display: flex; flex-direction: column; }
  .mail-sender { display: flex; align-items: center; gap: 14px; }
  .avatar { width: 66px; height: 66px; border-radius: 50%; background: radial-gradient(circle at 50% 40%, #8d8688, #2c2729); border: 3px solid #fff; flex-shrink: 0; }
  .sender-name { font-size: 24px; font-weight: 400; }
  .sender-date { font-size: 14px; color: var(--muted); margin-top: 4px; }
  .mail-body { margin-top: 16px; margin-left: 12px; border-left: 8px solid var(--plum); padding-left: 18px; padding-bottom: 8px; }
  .mail-subject { font-size: 20px; font-weight: 400; color: var(--plum-text); }
  .mail-text { margin-top: 12px; font-size: 14px; line-height: 1.6; text-align: justify; }
  .mail-text p { text-indent: 12px; }
  .mail-sign { margin-top: 14px; font-size: 14px; line-height: 1.7; }
  .mail-sign span { display: block; padding-left: 16px; }
  .attachments { margin-top: 12px; }
  .attachments h3 { font-size: 20px; font-weight: 500; display: flex; align-items: center; gap: 10px; }
  .attachments ul { list-style: none; margin-top: 8px; padding-left: 40px; }
  .attachments li { display: flex; align-items: center; gap: 14px; font-size: 15px; color: var(--muted); height: 32px; }
  .mail-actions {
    height: 70px; background: #ebe9ea; display: flex; align-items: center; gap: 50px; padding: 0 40px;
    font-size: 19px; color: var(--muted);
  }
  .mail-actions span { display: flex; align-items: center; gap: 10px; }
</style>
</head>
<body>
<main class="app-screens">

  <section class="screen">
    <div class="status-bar">
      <div class="status-left"><span class="signal">●●●●●</span> Corvo
        <svg width="18" height="13" viewBox="0 0 18 13"><path d="M1 4.5a11 11 0 0 1 16 0M4 7.5a7 7 0 0 1 10 0M7 10.5a3 3 0 0 1 4 0" fill="none" stroke="#2a2228" stroke-width="2" stroke-linecap="round"/></svg>
      </div>
      <div>9:23 AM</div>
      <div class="status-right"></div>
    </div>
    <header class="nav-bar">
      <span class="nav-back"><svg width="9" height="14" viewBox="0 0 9 14"><path d="M7 2 2 7l5 5" fill="none" stroke="#2a2228" stroke-width="2"/></svg>BACK</span>
      <span class="nav-title">SEND E-MAIL</span>
    </header>
    <div class="mail">
      <div class="mail-sender">
        <div class="avatar" role="img" aria-label="Profile photo of the sender"></div>
        <div>
          <div class="sender-name">From: Mara Lind</div>
          <div class="sender-date">10/03/2016</div>
        </div>
      </div>
      <div class="mail-body">
        <div class="mail-subject">Sub : Consultation derma</div>
        <div class="mail-text">
          <p>Lorem ipsum dolor sit amet, consectetur adipiscing elit. Aenean porta commodo scelerisque. Interdum et malesuada fames ante ipsum primis in faucibus. Morbi vitae maximus pretium, nec consectetur justo, vitae gravida nunc bibendum ante.</p>
          <p>Nam sit amet nibh sit amet mi tincidunt. Praesent mi elit, ultrices.</p>
        </div>
        <div class="mail-sign">Thanks,<span>Mara Lind</span></div>
        <div class="attachments">
          <h3><svg width="20" height="20" viewBox="0 0 20 20"><path d="M13 5 6 12a2 2 0 0 0 3 3l7-7a4 4 0 0 0-6-6L3 9a6 6 0 0 0 8 8l5-5" fill="none" stroke="#6d6469" stroke-width="1.6" stroke-linecap="round"/></svg>Attachments (2)</h3>
          <ul>
            <li><svg width="26" height="22" viewBox="0 0 26 22"><rect x="1" y="4" width="24" height="17" rx="3" fill="#3d2733"/><rect x="8" y="1" width="10" height="5" rx="1" fill="#3d2733"/><circle cx="13" cy="12.5" r="5" fill="#fff"/><circle cx="13" cy="12.5" r="2.6" fill="#3d2733"/></svg>image_001.jpg</li>
            <li><svg width="26" height="22" viewBox="0 0 26 22"><rect x="1" y="4" width="24" height="17" rx="3" fill="#3d2733"/><rect x="8" y="1" width="10" height="5" rx="1" fill="#3d2733"/><circle cx="13" cy="12.5" r="5" fill="#fff"/><circle cx="13" cy="12.5" r="2.6" fill="#3d2733"/></svg>image_002.jpg</li>
          </ul>
        </div>
      </div>
    </div>
    <div class="mail-actions">
      <span><svg width="24" height="24" viewBox="0 0 24 24"><path d="M14 4H4v16h16V10" fill="none" stroke="#6d6469" stroke-width="2"/><path d="m10 14 1-4 9-9 3 3-9 9z" fill="none" stroke="#6d6469" stroke-width="2"/></svg>Reply</span>
      <span><svg width="26" height="22" viewBox="0 0 26 22"><path d="M10 6H2v14h18v-5" fill="none" stroke="#6d6469" stroke-width="2"/><path d="M8 14c2-6 7-8 12-8V2l5 6-5 6V10c-5 0-9 1-12 4z" fill="none" stroke="#6d6469" stroke-width="2" stroke-linejoin="round"/></svg>Forward</span>
    </div>
    <nav class="partners"><a>Ostra</a><a>Toral</a><a>Lumavel</a><a>Norvexa</a></nav>
  </section>

  <section class="screen">
    <div class="status-bar">
      <div class="status-left"><span class="signal">●●●●●</span> Corvo
        <svg width="18" height="13" viewBox="0 0 18 13"><path d="M1 4.5a11 11 0 0 1 16 0M4 7.5a7 7 0 0 1 10 0M7 10.5a3 3 0 0 1 4 0" fill="none" stroke="#2a2228" stroke-width="2" stroke-linecap="round"/></svg>
      </div>
      <div>9:23 AM</div>
      <div class="status-right"></div>
    </div>
    <header class="nav-bar">
      <span class="nav-back"><svg width="9" height="14" viewBox="0 0 9 14"><path d="M7 2 2 7l5 5" fill="none" stroke="#2a2228" stroke-width="2"/></svg>BACK</span>
      <span class="nav-title">START SCREEN</span>
    </header>
    <div class="hero">
      <div class="hero-photo face" role="img" aria-label="Photo of a woman receiving a facial skin treatment"></div>
      <div class="hero-content">
        <div class="brand"><span class="brand-mark"></span><span class="brand-name">Vessa Kliniq</span></div>
        <div class="brand-tag">ONLINE DERMATOLOGY CONSULTATION</div>
        <div class="hero-heading">GET<br>DIAGNOSED</div>
      </div>
      <div class="carousel-dots"><span></span><span></span><span></span><span class="active"></span><span></span></div>
    </div>
    <ul class="menu">
      <li>START NEW CASE</li>
      <li>FOLLOW UP VISIT</li>
      <li>RX REFILL</li>
    </ul>
    <div class="shop-band">MEDICAL COSMETICS</div>
    <nav class="partners"><a>Ostra</a><a>Toral</a><a>Lumavel</a><a>Norvexa</a></nav>
    <div class="screen-foot"></div>
  </section>

  <section class="screen">
    <div class="status-bar">
      <div class="status-left"><span class="signal">●●●●●</span> Corvo
        <svg width="18" height="13" viewBox="0 0 18 13"><path d="M1 4.5a11 11 0 0 1 16 0M4 7.5a7 7 0 0 1 10 0M7 10.5a3 3 0 0 1 4 0" fill="none" stroke="#2a2228" stroke-width="2" stroke-linecap="round"/></svg>
      </div>
      <div>9:23 AM</div>
      <div class="status-right">
        <svg width="12" height="12" viewBox="0 0 12 12"><path d="M11 1 1 5.5l4.5 1 1 4.5z" fill="#2a2228"/></svg>66%
        <svg width="30" height="14" viewBox="0 0 30 14"><rect x="1" y="1" width="25" height="12" rx="2" fill="none" stroke="#2a2228" stroke-width="1.4"/><rect x="3" y="3" width="15" height="8" fill="#2a2228"/><rect x="27" y="5" width="2" height="4" fill="#2a2228"/></svg>
      </div>
    </div>
    <header class="nav-bar">
      <span class="nav-back"><svg width="9" height="14" viewBox="0 0 9 14"><path d="M7 2 2 7l5 5" fill="none" stroke="#2a2228" stroke-width="2"/></svg>BACK</span>
      <span class="nav-title">START SCREEN</span>
      <svg class="nav-search" width="24" height="24" viewBox="0 0 24 24"><circle cx="10" cy="10" r="8" fill="none" stroke="#2a2228" stroke-width="2"/><path d="m16 16 6 6" stroke="#2a2228" stroke-width="2"/></svg>
    </header>
    <div class="hero exam">
      <div class="hero-photo exam" role="img" aria-label="Photo of a dermatologist examining a patient's shoulder with a dermatoscope"></div>
      <div class="hero-content" style="top:50px">
        <div class="brand"><span class="brand-mark"></span><span class="brand-name">Vessa Kliniq</span></div>
        <div class="brand-tag">ONLINE DERMATOLOGY CONSULTATION</div>
        <div class="hero-heading" style="margin-top:46px">GET<br>DIAGNOSED</div>
      </div>
      <div class="carousel-dots"><span></span><span></span><span></span><span class="active"></span><span></span></div>
    </div>
    <ul class="menu">
      <li>START NEW CASE</li>
      <li>FOLLOW UP VISIT</li>
      <li>RX REFILL<svg width="10" height="16" viewBox="0 0 10 16"><path d="m2 2 6 6-6 6" fill="none" stroke="#2a2228" stroke-width="2"/></svg></li>
    </ul>
    <div class="shop-band long">MEDICAL COSMETICS SHOP</div>
    <nav class="partners"><a>Ostra</a><a>Toral</a><a>Lumavel</a><a>Norvexa</a></nav>
    <div class="screen-foot"></div>
  </section>

</main>
</body>
</html>
```